We sell companies excess stock for them

We need a business card for a company based in New Zealand called 'StockHarbor'.

Check out our website to get an idea www.stockharbor.example

We help other businesses to;
- Sell Excess Stock
- Manage Product Returns
- Sell Company Assets

Our logo is attached for your reference
The font used is 'RifficFree-Bold'

Target Market(s)

Businesses

Industry/Entity Type

Business

Contact Information for Business Card

Name: Mark Pellow
Phone: 027 846 2093
email: markpellow@stockharbor.example
website: www.stockharbor.example

Font styles to use
Other font styles liked:
• Unsure

Colors
9bcb3b

Requirements
Must have
• coming soon
Nice to have
• coming soon
Should not have
• coming soon

```html
<!DOCTYPE html>
<html lang="en">
<head>
<meta charset="utf-8">
<title>StockHarbor Business Card</title>
<link rel="stylesheet" href="https://fonts.googleapis.com/css2?family=Fredoka:wght@600&family=Roboto:wght@400;500;700&display=swap">
<style>
  :root {
    --page-bg: #d8d3cd;
    --card-top: #f4f5f3;
    --card-bottom: #e6e8e5;
    --ink: #1f1f1f;
    --text: #2b2b2b;
    --green: #5f9d1f;
    --green-bright: #9bcb3b;
    --art-green: #7fb13a;
    --art-orange: #e98a2c;
  }
  * { margin: 0; padding: 0; box-sizing: border-box; }
  html, body { width: 1200px; height: 969px; overflow: hidden; }
  body {
    background: var(--page-bg);
    font-family: "Roboto", Arial, sans-serif;
    position: relative;
  }
  .card {
    position: absolute;
    left: 100px; top: 199px;
    width: 1000px; height: 571px;
    border-radius: 30px;
    background: linear-gradient(160deg, var(--card-top), var(--card-bottom));
    box-shadow: 0 10px 30px rgba(0,0,0,0.18);
    overflow: hidden;
  }
  .mascot-art {
    position: absolute;
    left: 22px; top: 43px;
    width: 465px; height: 490px;
    border-radius: 40px;
    background: radial-gradient(circle at 45% 40%, var(--art-orange) 0%, rgba(233,138,44,0.55) 30%, var(--art-green) 65%, rgba(127,177,58,0.25) 100%);
    opacity: 0.85;
  }
  .brand {
    position: absolute;
    right: 75px; top: 52px;
    font-family: "Fredoka", "Arial Rounded MT Bold", sans-serif;
    font-weight: 600;
    font-size: 64px;
    letter-spacing: -0.5px;
    color: var(--ink);
    line-height: 1;
  }
  .name {
    position: absolute;
    right: 75px; top: 178px;
    font-weight: 700;
    font-size: 34px;
    letter-spacing: 0.5px;
    color: var(--ink);
    line-height: 1;
  }
  .name .surname { color: var(--green); }
  .side-tab {
    position: absolute;
    right: 0; top: 167px;
    width: 18px; height: 58px;
    border-radius: 9px 0 0 9px;
    background: var(--green-bright);
  }
  .contact {
    position: absolute;
    right: 75px; top: 248px;
    list-style: none;
    text-align: right;
  }
  .contact li {
    font-size: 24px;
    line-height: 31px;
    color: var(--text);
    display: flex;
    justify-content: flex-end;
    align-items: center;
    gap: 14px;
  }
  .contact svg { width: 20px; height: 20px; fill: var(--green); flex: none; }
  .services-title {
    position: absolute;
    right: 75px; top: 376px;
    font-weight: 700;
    font-size: 29px;
    color: var(--green);
    line-height: 1;
  }
  .services {
    position: absolute;
    right: 75px; top: 418px;
    list-style: none;
  }
  .services li {
    font-size: 24px;
    line-height: 33px;
    color: var(--text);
    display: flex;
    justify-content: flex-end;
    align-items: center;
    gap: 22px;
  }
  .services li::after {
    content: "";
    width: 8px; height: 8px;
    margin-right: 6px;
    border-radius: 50%;
    background: var(--green);
  }
</style>
</head>
<body>
  <div class="card">
    <div class="mascot-art" role="img" aria-label="Cartoon delivery mascot running with a parcel and giving a thumbs up"></div>

    <div class="brand">StockHarbor</div>
    <div class="name">MARK<span class="surname">PELLOW</span></div>
    <div class="side-tab"></div>

    <ul class="contact">
      <li>027 846 2093
        <svg viewBox="0 0 24 24" aria-hidden="true"><path d="M6.6 10.8a15.1 15.1 0 0 0 6.6 6.6l2.2-2.2a1 1 0 0 1 1-.25 11.4 11.4 0 0 0 3.6.57 1 1 0 0 1 1 1V20a1 1 0 0 1-1 1A17 17 0 0 1 3 4a1 1 0 0 1 1-1h3.5a1 1 0 0 1 1 1c0 1.25.2 2.45.57 3.57a1 1 0 0 1-.25 1z"/></svg>
      </li>
      <li>markpellow@stockharbor.example
        <svg viewBox="0 0 24 24" aria-hidden="true"><path d="M2 5h20v14H2z M3.5 6.5 12 12.5l8.5-6z" fill-rule="evenodd"/><path d="M2 5h20L12 12z" opacity="0.7"/></svg>
      </li>
      <li>www.stockharbor.example
        <svg viewBox="0 0 24 24" aria-hidden="true"><circle cx="12" cy="12" r="10"/><path d="M4 12h16M12 2c3 3 3 17 0 20M12 2c-3 3-3 17 0 20" stroke="#eef0ee" stroke-width="1.6" fill="none"/></svg>
      </li>
    </ul>

    <div class="services-title">We help other businesses to</div>
    <ul class="services">
      <li>Sell Excess Stock</li>
      <li>Manage Product Returns</li>
      <li>Sell Company Assets</li>
    </ul>
  </div>
</body>
</html>
```